Dental Business Card

I need Dental oriented business cards.
On the front side -
- on the first line, my name:
Dr Marlo Vintner
- on the second line (just underneath):
Doctor of Dental Medicine
- on the third line, or underneath that or in a corner, I would like the address and phone number:
5182 Ch. Birchfield
Montreal QC H2T 4B9
514-629-5074
- other than that i would maybe like a logo of a tooth, but i want it to be subtle and very basic!
- I would like the card to be preferably black or dark grey-ish with the writing in white
On the other side -
- 2-3 lines with the possibility to write the next appointment the box with the lines should be white, with the rest of the card being black

```html
<!DOCTYPE html>
<html lang="en">
<head>
<meta charset="utf-8">
<title>Dr Marlo Vintner – Business Card</title>
<link href="https://fonts.googleapis.com/css2?family=Oswald:wght@500&family=Jost:wght@400;500&display=swap" rel="stylesheet">
<style>
  :root {
    --page-bg: #e4e4e4;
    --card-dark: #1c1d1e;
    --card-mid: #2e2e2f;
    --accent: #3bb9e6;
    --accent-deep: #1a8fd6;
    --ink: #ffffff;
  }
  * { box-sizing: border-box; margin: 0; padding: 0; }
  html, body {
    width: 1200px; height: 1200px; overflow: hidden;
    background: var(--page-bg);
    font-family: "Jost", sans-serif;
    color: var(--ink);
  }
  .card {
    position: absolute; left: 120px; width: 960px; height: 548px;
    border-radius: 34px; overflow: hidden;
    background: linear-gradient(120deg, var(--card-dark) 0%, var(--card-mid) 100%);
    box-shadow: 0 10px 24px rgba(0,0,0,.25);
  }
  .card--front { top: 40px; }
  .card--back { top: 612px; }

  /* Front */
  .identity { position: absolute; left: 150px; top: 170px; padding-left: 34px; }
  .identity__bar {
    position: absolute; left: 0; top: 6px; width: 9px; height: 72px;
    background: var(--accent-deep);
  }
  .identity__name {
    font-family: "Oswald", sans-serif; font-weight: 500; font-size: 54px;
    line-height: 1; text-transform: uppercase; letter-spacing: .5px;
    background: linear-gradient(90deg, var(--accent-deep), var(--accent));
    -webkit-background-clip: text; background-clip: text; color: transparent;
  }
  .identity__title { font-size: 25px; margin-top: 10px; letter-spacing: .5px; }
  .contact { position: absolute; left: 150px; top: 330px; font-size: 22px; letter-spacing: .6px; }
  .contact__row { display: flex; align-items: center; gap: 14px; margin-bottom: 16px; }
  .contact__icon { width: 18px; height: 18px; flex: none; }
  .brand {
    position: absolute; right: 90px; top: 150px;
    display: flex; align-items: center; gap: 14px;
    font-size: 30px; font-weight: 500; color: var(--accent);
  }
  .brand__dot { width: 22px; height: 22px; border-radius: 50%; background: var(--accent); }

  /* Back */
  .band { position: absolute; left: 0; top: 0; width: 100%; height: 30px; background: var(--accent); }
  .appointment__heading {
    position: absolute; left: 100px; top: 95px;
    font-size: 36px; font-weight: 400; color: var(--accent); letter-spacing: .5px;
  }
  .field-label { position: absolute; font-size: 24px; letter-spacing: .5px; }
  .field-box { position: absolute; height: 42px; background: var(--ink); }
  .check { position: absolute; width: 36px; height: 36px; background: var(--ink); }
  .address-line {
    position: absolute; left: 0; right: 0; bottom: 48px;
    text-align: center; font-size: 26px; font-weight: 500; letter-spacing: .8px;
  }
</style>
</head>
<body>

<section class="card card--front" aria-label="Card front">
  <div class="identity">
    <span class="identity__bar"></span>
    <h1 class="identity__name">Dr Marlo Vintner</h1>
    <p class="identity__title">Doctor of Dental Medicine</p>
  </div>

  <div class="contact">
    <div class="contact__row">
      <svg class="contact__icon" viewBox="0 0 24 24" aria-hidden="true">
        <path fill="#3bb9e6" d="M6.6 10.8a15.1 15.1 0 0 0 6.6 6.6l2.2-2.2a1 1 0 0 1 1-.25 11.4 11.4 0 0 0 3.6.57 1 1 0 0 1 1 1V20a1 1 0 0 1-1 1A17 17 0 0 1 3 4a1 1 0 0 1 1-1h3.5a1 1 0 0 1 1 1c0 1.25.2 2.45.57 3.57a1 1 0 0 1-.25 1z"/>
      </svg>
      <span>514-629-5074</span>
    </div>
    <div class="contact__row">
      <svg class="contact__icon" viewBox="0 0 24 24" aria-hidden="true">
        <path fill="#3bb9e6" d="M12 2a7 7 0 0 0-7 7c0 5.25 7 13 7 13s7-7.75 7-13a7 7 0 0 0-7-7zm0 9.5A2.5 2.5 0 1 1 12 6.5a2.5 2.5 0 0 1 0 5z"/>
      </svg>
      <span>5182 Ch. Birchfield Montreal QC H2T 4B9</span>
    </div>
  </div>

  <div class="brand">
    <span class="brand__dot"></span>
    <span>Vintner Dental</span>
  </div>
</section>

<section class="card card--back" aria-label="Card back">
  <div class="band"></div>
  <h2 class="appointment__heading">Next Appointment</h2>

  <span class="field-label" style="left:80px; top:178px;">Name</span>
  <div class="field-box" style="left:170px; top:176px; width:720px;"></div>

  <span class="field-label" style="left:80px; top:268px;">Date</span>
  <div class="field-box" style="left:170px; top:266px; width:290px;"></div>

  <span class="field-label" style="left:500px; top:268px;">Time</span>
  <div class="field-box" style="left:580px; top:266px; width:310px;"></div>

  <div class="check" style="left:600px; top:340px;"></div>
  <span class="field-label" style="left:648px; top:342px;">AM</span>
  <div class="check" style="left:730px; top:340px;"></div>
  <span class="field-label" style="left:778px; top:342px;">PM</span>

  <p class="address-line">5182 Ch. Birchfield Montreal QC H2T 4B9</p>
</section>

</body>
</html>
```